Meridel Hair Studio Needs a new appointment business card

We need a new appointment card for our hair salon.

I Dont want bright out there colours.
I would like it to be neat, clean, easy to read. White, Black, with a hint of colour if needed.

We need
-Logo
-Phone number 47208613
-Mobile Number: 0417306852
Address: Shop 3/214 Calder Road, The Elmgates, Brenford 4812

BACK SIDE OF CARD
- Appointment Time & Date (White background so we are able to write on it)
(If you are unable to make your appointment please contact us ASAP 47208613)

I also would like the chatterly and Pictorama logo(Find us on Chatterly)(find us on Pictorama)

Target Market(s)

appointment card simple to read. all information for their next appoint For all our clients male and female

Industry/Entity Type

Hairdresser

Contact Information for Business Card

-Logo
-Phone number 47208613

BACK SIDE OF CARD

Font styles to use
Serif
Sans Serif
Script

Requirements
Must have
• White Back ground on backside with appointment deatils so we are able to write information (like appointment time and date)
Nice to have
• Find us on Chatterly
and
pictorama - meridel_hairstudio
Should not have
• BRIGHT COLOURS

```html
<!DOCTYPE html>
<html lang="en">
<head>
<meta charset="utf-8">
<title>Meridel Hair Studio – Appointment Card</title>
<link rel="stylesheet" href="https://fonts.googleapis.com/css2?family=Poppins:wght@400;500&display=swap">
<style>
  :root {
    --page: #e4e4e2;
    --card: #f1f1ef;
    --ink: #6a6a6a;
    --ink-dark: #5a5a5a;
    --accent: #d6bb98;
    --band: #ebe2d6;
  }
  * { box-sizing: border-box; margin: 0; padding: 0; }
  html, body { width: 1200px; height: 800px; overflow: hidden; }
  body {
    background: var(--page);
    font-family: "Poppins", sans-serif;
    color: var(--ink);
    display: flex;
    align-items: center;
    justify-content: center;
    gap: 50px;
  }
  .card {
    position: relative;
    width: 530px;
    height: 303px;
    background: var(--card);
    box-shadow: 0 6px 18px rgba(0,0,0,0.12);
    overflow: hidden;
    text-align: center;
  }
  .tool-band {
    position: absolute;
    left: 0; right: 0; bottom: 0;
    height: 44px;
    background: linear-gradient(90deg, var(--band), #efe8de, var(--band));
  }

  /* front */
  .card-front .brand {
    margin-top: 78px;
    font-size: 38px;
    font-weight: 400;
    letter-spacing: 3px;
    color: var(--ink-dark);
    line-height: 1;
  }
  .card-front .brand-sub {
    display: block;
    margin-top: 6px;
    font-size: 13px;
    letter-spacing: 6px;
  }
  .card-front .dash {
    width: 22px; height: 3px;
    background: var(--accent);
    margin: 16px auto 14px;
  }
  .card-front .contact {
    font-size: 11.5px;
    letter-spacing: 0.6px;
    line-height: 1.7;
  }

  /* back */
  .appointment-box {
    margin: 30px auto 0;
    width: 290px;
    border: 1px solid var(--accent);
    padding: 18px 24px 22px;
    text-align: left;
  }
  .appointment-box h2 {
    font-size: 15px;
    font-weight: 400;
    letter-spacing: 1.2px;
    text-align: center;
    margin-bottom: 12px;
  }
  .field {
    display: flex;
    align-items: flex-end;
    font-size: 13px;
    letter-spacing: 0.8px;
    margin-top: 8px;
  }
  .field-label { width: 50px; }
  .blank {
    flex: 1;
    border-bottom: 1px solid var(--ink);
    height: 14px;
  }
  .slash { padding: 0 6px; font-size: 12px; }
  .notice {
    font-size: 11px;
    letter-spacing: 0.5px;
    line-height: 1.45;
    margin-top: 12px;
  }
  .find-us {
    font-size: 11px;
    letter-spacing: 0.5px;
    margin-top: 10px;
  }
  .network {
    display: inline-flex;
    align-items: center;
    gap: 4px;
    margin-left: 6px;
  }
  .network-dot {
    width: 7px; height: 7px;
    background: var(--accent);
  }
  .handle {
    font-size: 10.5px;
    letter-spacing: 0.5px;
    margin-top: 2px;
  }
</style>
</head>
<body>

  <section class="card card-front" aria-label="Card front">
    <h1 class="brand">MERIDEL<span class="brand-sub">HAIR STUDIO</span></h1>
    <div class="dash"></div>
    <p class="contact">Tel. 47208613&nbsp;&nbsp;Mobile. 0417306852</p>
    <p class="contact">Address. Shop 3/214 Calder Road, The Elmgates, Brenford 4812</p>
    <div class="tool-band" role="img" aria-label="Repeating row of hair salon tool icons: scissors, dryer, brush, mirror, comb"></div>
  </section>

  <section class="card card-back" aria-label="Card back">
    <div class="appointment-box">
      <h2>Your Next Appointment:</h2>
      <div class="field">
        <span class="field-label">Date:</span>
        <span class="blank"></span><span class="slash">/</span>
        <span class="blank"></span><span class="slash">/</span>
        <span class="blank"></span>
      </div>
      <div class="field">
        <span class="field-label">Time:</span>
        <span class="blank"></span>
      </div>
    </div>
    <p class="notice">If you are unable to make your appointment<br>please contact us ASAP 47208613</p>
    <p class="find-us">Find us on
      <span class="network"><span class="network-dot"></span>Chatterly</span>
      <span class="network"><span class="network-dot"></span>Pictorama</span>
    </p>
    <p class="handle">meridel_hairstudio</p>
    <div class="tool-band" role="img" aria-label="Repeating row of hair salon tool icons: scissors, dryer, brush, mirror, comb"></div>
  </section>

</body>
</html>
```